Business Card Design

We need business cards designed incorporating our graphics/logo already used on our trucks. We are a small construction company that does everything from building new homes, additions, Kitchens, Baths, Decks, Hardwood Floors/Tile, all phases of construction. No job is too small. We pride ourselves on True Craftmanship/Customer Satisfaction, its what truly separates us from everyone else.

Industry/Entity Type

Construction

Contact Information for Business Card

Maple Ridge Renovations Lic#27KT51986400
342 51st Avenue Cedar Cove NJ 08099
(555)317-2984 Email: info@mapleridgellc.example
Paul Tremondale

```html
<!DOCTYPE html>
<html lang="en">
<head>
<meta charset="utf-8">
<title>Maple Ridge Renovations – Business Cards</title>
<link rel="stylesheet" href="https://fonts.googleapis.com/css2?family=Archivo+Black&family=Marcellus&family=Open+Sans:wght@400;600&display=swap">
<style>
  :root {
    --backdrop: #161616;
    --sky: #a9d8ef;
    --sky-deep: #8cc7e6;
    --sand: #e9ac6d;
    --sand-deep: #d9955a;
    --wave-line: #2b2b2b;
    --brand-gold: #c9a545;
    --ink: #2c2c2c;
    --badge: #6cc3ea;
    --bullet: #3a3a3a;
    --card-w: 560px;
    --card-h: 320px;
  }
  * { box-sizing: border-box; margin: 0; padding: 0; }
  html, body { width: 1200px; height: 872px; overflow: hidden; }
  body {
    background: var(--backdrop);
    position: relative;
    font-family: "Open Sans", sans-serif;
    color: var(--ink);
  }
  .card {
    position: absolute;
    left: 320px;
    width: var(--card-w);
    height: var(--card-h);
    overflow: hidden;
    border-radius: 4px;
    background: var(--sand);
  }
  .card--back { top: 96px; }
  .card--front { top: 456px; }

  /* Back side */
  .back-scene { position: absolute; inset: 0; }
  .back-brand {
    position: absolute;
    left: 40px;
    top: 34px;
    font-family: "Archivo Black", sans-serif;
    font-size: 38px;
    line-height: 1.18;
    letter-spacing: 2px;
    color: var(--brand-gold);
    text-align: center;
  }
  .crew-artwork {
    position: absolute;
    right: 26px;
    bottom: 52px;
    width: 170px;
    height: 112px;
    border-radius: 6px;
    background: linear-gradient(160deg, #5b6f9a, #8a7a5a);
  }
  .service-list {
    position: absolute;
    left: 30px;
    top: 196px;
    list-style: none;
    font-family: "Archivo Black", sans-serif;
    font-size: 18px;
    letter-spacing: 2px;
    color: #ffffff;
  }
  .service-list li {
    display: flex;
    align-items: center;
    gap: 14px;
    margin-bottom: 8px;
  }
  .service-list li::before {
    content: "";
    width: 12px; height: 12px;
    border-radius: 50%;
    background: var(--bullet);
  }

  /* Front side */
  .front-top {
    position: absolute;
    left: 0; top: 0;
    width: 100%; height: 152px;
    background: linear-gradient(180deg, var(--sky), var(--sky-deep));
    display: flex;
    align-items: center;
    justify-content: center;
  }
  .front-brand {
    font-family: "Archivo Black", sans-serif;
    font-size: 38px;
    line-height: 1.2;
    letter-spacing: 3px;
    color: var(--brand-gold);
    text-align: center;
  }
  .front-bottom {
    position: absolute;
    left: 0; top: 152px;
    width: 100%; height: 168px;
    background: linear-gradient(180deg, var(--sand), var(--sand-deep));
  }
  .holder-name {
    position: absolute;
    left: 28px;
    top: 40px;
    font-family: "Marcellus", serif;
    font-size: 21px;
  }
  .divider {
    position: absolute;
    left: 232px;
    top: 16px;
    width: 1px;
    height: 132px;
    background: var(--ink);
  }
  .contact-list {
    position: absolute;
    left: 250px;
    top: 16px;
    right: 16px;
    list-style: none;
    font-size: 14.5px;
    line-height: 1.3;
  }
  .contact-list li {
    display: flex;
    gap: 12px;
    margin-bottom: 9px;
  }
  .badge {
    flex: none;
    width: 18px; height: 18px;
    background: var(--badge);
    color: var(--ink);
    font-weight: 600;
    font-size: 12px;
    display: flex;
    align-items: center;
    justify-content: center;
  }
</style>
</head>
<body>

<section class="card card--back" aria-label="Business card, back">
  <svg class="back-scene" width="560" height="320" viewBox="0 0 560 320" aria-hidden="true">
    <rect width="560" height="320" fill="var(--sand)"/>
    <path d="M0 0 H560 V120 C470 112 400 150 300 158 C200 166 80 150 0 196 Z" fill="var(--sky)"/>
    <path d="M560 120 C470 112 400 150 300 158 C200 166 80 150 0 196" fill="none" stroke="var(--wave-line)" stroke-width="3"/>
  </svg>
  <div class="back-brand">MAPLE RIDGE<br>RENOVATIONS</div>
  <div class="crew-artwork" role="img" aria-label="Illustration of two builders in hard hats holding lumber"></div>
  <ul class="service-list">
    <li>REMODELING</li>
    <li>DECKS</li>
    <li>ADDITIONS</li>
  </ul>
</section>

<section class="card card--front" aria-label="Business card, front">
  <div class="front-top">
    <div class="front-brand">MAPLE RIDGE<br>RENOVATIONS</div>
  </div>
  <div class="front-bottom">
    <p class="holder-name">Paul Tremondale</p>
    <span class="divider"></span>
    <ul class="contact-list">
      <li><span class="badge">A</span><span>Lic#27KT51986400 342 51st Avenue<br>Cedar Cove NJ 08099</span></li>
      <li><span class="badge">T</span><span>(555)317-2984</span></li>
      <li><span class="badge">E</span><span>info@mapleridgellc.example</span></li>
    </ul>
  </div>
</section>

</body>
</html>
```